Author needs a new book, Kindle and Audiobook cover design

I updated and re-edited a book I wrote 25 years ago but now realize the title and design did not get the job done. I am seeking a book, Kindle and audiobook design that will make me stand out. The final design will pop while being sensitive to the nature of the subject. The title of the book is Quiet Lanterns. Subtitle: Ways to Notice and Step Away From Harmful Circles While Keeping Steady Belief by Dorian T. Wexcombe. I am wanting to get the attention of people who have been damaged by a church relationship that started well but ended badly.
Updates

The book title is: Quiet Lanterns. The Subtitle is: Ways To Notice and Step Away From Harmful Circles While Keeping Steady Belief. The dimension is 6x9 (150 pages) and I am the author: Dorian T. Wexcombe

Target Market(s)

People with a church experience; church leadership. Religious abuse victims.

Industry/Entity Type

Christian

Font styles to use
Serif

Colors

Designer to choose colors to be used in the design.

Requirements
Nice to have
• I am not married to the Serif font if another design works better.

```html
<!DOCTYPE html>
<html lang="en">
<head>
<meta charset="UTF-8">
<title>Quiet Lanterns — Book Cover</title>
<link rel="stylesheet" href="https://fonts.googleapis.com/css2?family=Cinzel:wght@500&family=Arimo:wght@400&family=Libre+Baskerville:wght@700&display=swap">
<style>
  :root {
    --page-bg: #ffffff;
    --cover-black: #0b0907;
    --cave-dark: #1a120b;
    --cave-brown: #5a3a1e;
    --cave-amber: #c9853f;
    --light-glow: #fff6e4;
    --title-gold: #f4e7a6;
    --subtitle-white: #f2f2f2;
  }
  * { box-sizing: border-box; margin: 0; padding: 0; }
  html, body {
    width: 1200px;
    height: 1000px;
    overflow: hidden;
    background: var(--page-bg);
  }
  .canvas {
    position: relative;
    width: 1200px;
    height: 1000px;
  }
  .book-cover {
    position: absolute;
    left: 300px;
    top: 50px;
    width: 600px;
    height: 900px;
    background: var(--cover-black);
    overflow: hidden;
    box-shadow: 0 10px 30px rgba(0, 0, 0, 0.35);
  }
  .cover-scene {
    position: absolute;
    inset: 0;
    background:
      radial-gradient(ellipse 90px 190px at 46% 50%, var(--light-glow) 0%, #ffe9bf 45%, rgba(255, 220, 160, 0) 100%),
      radial-gradient(ellipse 260px 330px at 46% 52%, rgba(201, 133, 63, 0.85) 0%, rgba(90, 58, 30, 0.7) 45%, rgba(26, 18, 11, 0) 100%),
      linear-gradient(160deg, rgba(255, 255, 255, 0.08) 30%, rgba(255, 255, 255, 0) 60%),
      radial-gradient(ellipse 420px 520px at 46% 55%, var(--cave-dark) 0%, var(--cover-black) 100%);
  }
  .cover-title {
    position: absolute;
    top: 58px;
    left: 0;
    width: 100%;
    text-align: center;
    font-family: "Cinzel", "Times New Roman", serif;
    font-weight: 500;
    font-size: 52px;
    letter-spacing: 1px;
    color: var(--title-gold);
    white-space: nowrap;
  }
  .cover-subtitle {
    position: absolute;
    top: 150px;
    left: 40px;
    right: 40px;
    text-align: center;
    font-family: "Arimo", Arial, sans-serif;
    font-size: 19px;
    line-height: 30px;
    color: var(--subtitle-white);
  }
  .cover-author {
    position: absolute;
    bottom: 52px;
    left: 0;
    width: 100%;
    text-align: center;
    font-family: "Libre Baskerville", Georgia, serif;
    font-weight: 700;
    font-size: 34px;
    color: var(--title-gold);
  }
</style>
</head>
<body>
  <main class="canvas">
    <article class="book-cover">
      <div class="cover-scene" role="img" aria-label="Photograph of a dark rocky cave opening with bright warm light pouring in from outside and rays of light falling across the stony floor"></div>
      <h1 class="cover-title">QUIET LANTERNS</h1>
      <p class="cover-subtitle">Ways To Notice and Step Away From Harmful Circles While Keeping Steady Belief</p>
      <p class="cover-author">Dorian T. Wexcombe</p>
    </article>
  </main>
</body>
</html>
```